We need a business card and letterhead design for an orthodontic office. Needs to be clean, simple and sleek

Target Market(s)

adults/children

Industry/Entity Type

Dental

Contact Information for Business Card

Logo that is attached

Font styles to use
Serif

Colors

Designer to choose colors to be used in the design.

Requirements
Must have
• Peter L Vantrell DDS
• Corinne Palk DMD
• 82 Tolland Avenue
• Alderton,OR 97345
• (541) 555-0196
• www.vantrellortho.example
Nice to have
• on the back.... space for appointment times
Should not have
• teeth

```html
<!DOCTYPE html>
<html lang="en">
<head>
<meta charset="utf-8">
<title>Peter Vantrell Orthodontics – Stationery</title>
<link href="https://fonts.googleapis.com/css2?family=Quicksand:wght@300;400;600;700&display=swap" rel="stylesheet">
<style>
  :root{
    --bg:#e4e1e3;
    --paper:#ffffff;
    --blue:#66a3ca;
    --charcoal:#37383b;
    --ink:#2c2d30;
    --muted:#6b6d72;
  }
  *{box-sizing:border-box;margin:0;padding:0}
  html,body{width:1200px;height:842px;overflow:hidden;background:var(--bg)}
  body{position:relative;font-family:"Quicksand",sans-serif;color:var(--ink)}

  /* ---------- Letterhead ---------- */
  .letterhead{position:absolute;left:620px;top:52px;width:520px;height:738px;background:var(--paper);overflow:hidden;
    box-shadow:0 2px 6px rgba(0,0,0,.12)}
  .letterhead__band{position:absolute;left:0;top:0;width:520px;height:95px}
  .wordmark{font-family:"Quicksand",sans-serif;font-weight:300;color:var(--charcoal);text-transform:uppercase;line-height:1}
  .letterhead .wordmark{position:absolute;right:34px;top:40px;width:190px}
  .letterhead .wordmark__name{font-size:28px;letter-spacing:4px;display:block}
  .letterhead .wordmark__sub{font-size:12.5px;letter-spacing:2.4px;display:block;margin-top:5px}
  .sender{position:absolute;left:58px;top:140px;font-size:10.5px;line-height:1.35}
  .sender strong{font-weight:700}
  .sender__address{margin-top:10px}
  .letter-body{position:absolute;left:58px;top:218px;width:380px;font-size:10px;line-height:1.55;color:var(--ink)}
  .letter-body p{margin-bottom:14px}
  .signoff{position:absolute;left:58px;top:570px;font-size:11px;line-height:1.4}
  .letter-footer{position:absolute;left:58px;bottom:40px;font-size:8.5px;font-weight:600;line-height:1.5}
  .letter-footer .tag{color:var(--blue);font-weight:700;margin-right:3px}
  .letter-footer .gap{margin-left:14px}
  .letterhead__base{position:absolute;left:0;bottom:0;width:100%;height:22px;background:var(--charcoal)}

  /* ---------- Business cards ---------- */
  .card{position:absolute;left:70px;width:420px;height:240px;background:var(--paper);overflow:hidden;
    box-shadow:0 2px 6px rgba(0,0,0,.12)}
  .card--front{top:110px}
  .card--back{top:440px}
  .card__art{position:absolute;inset:0;width:420px;height:240px}
  .card--front .wordmark{position:absolute;left:0;right:0;top:52px;text-align:center}
  .card--front .wordmark__name{font-size:34px;letter-spacing:6px;display:block}
  .card--front .wordmark__sub{font-size:14px;letter-spacing:3px;display:block;margin-top:4px}
  .card__web{position:absolute;left:0;right:0;top:178px;text-align:center;color:#fff;font-size:10px;font-weight:600;letter-spacing:.3px}
  .card__web i{display:inline-block;width:7px;height:7px;border-radius:50%;background:#fff;margin-right:5px;vertical-align:0}

  .card--back .wordmark{position:absolute;left:95px;top:120px;transform:translate(-50%,-50%) rotate(-90deg);white-space:nowrap;color:#fff}
  .card--back .wordmark__name{font-size:30px;letter-spacing:5px;display:block}
  .card--back .wordmark__sub{font-size:12.5px;letter-spacing:2.4px;display:block;margin-top:4px}
  .card__details{position:absolute;left:205px;top:34px;width:150px;text-align:right;font-size:9px;color:var(--muted);line-height:1.4}
  .person{font-size:12px;color:var(--ink);font-weight:300;text-transform:uppercase;line-height:1.1}
  .person b{font-weight:700}
  .person__title{font-size:8px;color:var(--muted);display:block;margin-bottom:6px}
  .card__details .rule{height:1px;background:#cfd0d3;margin:6px 0 6px 40px}
  .card__icons{position:absolute;left:372px;top:70px;width:30px;display:flex;flex-direction:column;align-items:center;gap:16px}
</style>
</head>
<body>

<section class="letterhead" aria-label="Letterhead">
  <svg class="letterhead__band" viewBox="0 0 520 95" aria-hidden="true">
    <path d="M0 0H520V24H300C282 24 278 32 272 46C266 60 258 68 236 68H0Z" fill="var(--blue)"/>
  </svg>
  <div class="wordmark">
    <span class="wordmark__name">Peter</span>
    <span class="wordmark__name">Vantrell</span>
    <span class="wordmark__sub">Orthodontics</span>
  </div>

  <div class="sender">
    <strong>Peter L Vantrell</strong><br>DDS
    <div class="sender__address">82 Tolland Avenue<br>Alderton,OR 97345</div>
  </div>

  <div class="letter-body">
    <p>Lorem Ipsum is simply dummy text for printing and typesetting industry. Lorem Ipsum has been the industry's standard dummy text since the 1500s, when an unknown printer galley of type and scrambled it to make a type specimen book. It has suvived not only manual but also the leap into electronic typesetting, remaining essentially un changed. It was popularised in the 1960s with the release of Transfera sheets containing Lorem Ipsum pass and more recently with desktop publishing software like Folio Layout including version 6.9 of Lorem Ipsum.</p>
    <p>Country to popular belief, Lorem Ipsum is not simply random text. It has roots in a piece of sical Latin literature from 45 BC, making it over 2000 years old. Howard Lindqvist, a prfessor at Ashbury College in Virginia, looked up one of the most of the world classical literature, discovered the undoubtable sorce. Lorem Ipsum comes from section 1.10.32 and 1.10.33 of "de Finibus Bonorum et Malorum" (The Extreme of Good and Even Cicero), written in 45 BC. This book is a treatise on the theory of ethics very popular during Renassiance.</p>
    <p>Thank you for being one of our valued customers.</p>
  </div>

  <div class="signoff">Name Here<br>CEO</div>

  <div class="letter-footer">
    82 Tolland Avenue Alderton,OR 97345<br>
    <span class="tag">P</span>(541) 555-0196<span class="gap"></span><span class="tag">W</span>www.vantrellortho.example
  </div>
  <div class="letterhead__base"></div>
</section>

<section class="card card--front" aria-label="Business card front">
  <svg class="card__art" viewBox="0 0 420 240" aria-hidden="true">
    <rect x="0" y="14" width="28" height="6" fill="var(--blue)"/>
    <rect x="392" y="14" width="28" height="6" fill="var(--blue)"/>
    <path d="M0 194H92C104 194 106 172 122 168H298C314 172 316 194 328 194H420V240H0Z" fill="var(--blue)"/>
  </svg>
  <div class="wordmark">
    <span class="wordmark__name">Peter</span>
    <span class="wordmark__name">Vantrell</span>
    <span class="wordmark__sub">Orthodontics</span>
  </div>
  <div class="card__web"><i></i>www.vantrellortho.example</div>
</section>

<section class="card card--back" aria-label="Business card back">
  <svg class="card__art" viewBox="0 0 420 240" aria-hidden="true">
    <rect x="0" y="0" width="190" height="240" fill="var(--charcoal)"/>
    <path d="M190 0H420V240H190V214C190 206 196 202 202 202V38C196 38 190 34 190 26Z" fill="var(--paper)"/>
    <rect x="190" y="0" width="20" height="18" fill="var(--blue)"/>
    <path d="M366 0H420V240H366V206C366 200 372 196 378 196H382V44H378C372 44 366 40 366 34Z" fill="var(--blue)"/>
  </svg>
  <div class="wordmark">
    <span class="wordmark__name">Peter</span>
    <span class="wordmark__name">Vantrell</span>
    <span class="wordmark__sub">Orthodontics</span>
  </div>
  <div class="card__details">
    <div class="person">Peter L <b>Vantrell</b></div>
    <span class="person__title">DDS</span>
    <div class="person">Corinne <b>Palk</b></div>
    <span class="person__title">DMD</span>
    <div>(541) 555-0196</div>
    <div class="rule"></div>
    <div>www.vantrellortho.example</div>
    <div class="rule"></div>
    <div>82 Tolland Avenue<br>Alderton,OR 97345</div>
  </div>
  <div class="card__icons" aria-hidden="true">
    <svg width="12" height="12" viewBox="0 0 12 12"><path d="M3 1l2 2.5-1.2 1.2a7 7 0 0 0 3.5 3.5L8.5 7 11 9l-1.2 2C5 11 1 7 1 2.2Z" fill="#fff"/></svg>
    <svg width="2" height="10"><rect width="1" height="10" fill="#fff"/></svg>
    <svg width="12" height="12" viewBox="0 0 12 12"><circle cx="6" cy="6" r="5" fill="none" stroke="#fff" stroke-width="1.2"/><path d="M1 6h10M6 1c-2.5 3-2.5 7 0 10M6 1c2.5 3 2.5 7 0 10" fill="none" stroke="#fff" stroke-width="1"/></svg>
    <svg width="2" height="10"><rect width="1" height="10" fill="#fff"/></svg>
    <svg width="12" height="12" viewBox="0 0 12 12"><path d="M6 11.5C3 8 2 6.2 2 4.5a4 4 0 0 1 8 0c0 1.7-1 3.5-4 7Z" fill="#fff"/><circle cx="6" cy="4.5" r="1.5" fill="var(--blue)"/></svg>
  </div>
</section>

</body>
</html>
```